Construction business card

I need a new business card, they can connect with my logo, brand.
What we do is residential house , design and build
I like: Navy blue / black
I attached our logo, brand,
and, some idea for business card.

```html
<!DOCTYPE html>
<html lang="en">
<head>
<meta charset="utf-8">
<title>Harbourline Homes – Business Card</title>
<link rel="stylesheet" href="https://fonts.googleapis.com/css2?family=Lato:wght@400;700&display=swap">
<style>
  :root {
    --stage: #1f1f1f;
    --card: #161616;
    --card-edge: #1b1b1b;
    --pattern-a: #1a1a1a;
    --pattern-b: #222222;
    --accent: #2f80ff;
    --ink: #ffffff;
    --mark-dim: #2e2e2e;
  }
  * { box-sizing: border-box; margin: 0; padding: 0; }
  html, body {
    width: 1200px;
    height: 897px;
    overflow: hidden;
    background: var(--stage);
    font-family: "Lato", sans-serif;
  }
  .canvas {
    position: relative;
    width: 1200px;
    height: 897px;
  }
  .card {
    position: absolute;
    left: 300px;
    width: 600px;
    height: 343px;
    border-radius: 18px;
    background: var(--card);
    box-shadow: 0 10px 30px rgba(0,0,0,0.45);
    overflow: hidden;
  }
  .card--back { top: 55px; }
  .card--front { top: 470px; }

  .back-pattern {
    position: absolute;
    inset: 0;
    background: linear-gradient(135deg, var(--pattern-b), var(--pattern-a) 55%, var(--pattern-b));
  }
  .back-brand {
    position: absolute;
    left: 430px;
    top: 236px;
    color: var(--ink);
    font-weight: 700;
    font-size: 13px;
    letter-spacing: 1px;
    text-transform: uppercase;
    line-height: 1.2;
    text-align: center;
    width: 110px;
  }

  .holder-name {
    position: absolute;
    left: 44px;
    top: 40px;
    color: var(--accent);
    font-weight: 700;
    font-size: 30px;
    letter-spacing: 1px;
    text-transform: uppercase;
  }
  .holder-role {
    position: absolute;
    left: 44px;
    top: 80px;
    color: var(--ink);
    font-size: 17px;
  }
  .address {
    position: absolute;
    left: 44px;
    top: 132px;
    color: var(--ink);
    font-size: 17px;
    line-height: 1.35;
  }
  .contacts {
    position: absolute;
    left: 44px;
    top: 212px;
    list-style: none;
  }
  .contact {
    display: flex;
    align-items: center;
    gap: 16px;
    color: var(--ink);
    font-size: 17px;
    height: 30px;
  }
  .contact-icon { width: 20px; height: 20px; fill: var(--accent); flex: none; }

  .front-brand {
    position: absolute;
    right: 40px;
    bottom: 52px;
    width: 260px;
    color: var(--mark-dim);
    font-weight: 700;
    font-size: 40px;
    line-height: 1.05;
    text-transform: uppercase;
    text-align: center;
    letter-spacing: 1px;
  }
</style>
</head>
<body>
<main class="canvas">
  <section class="card card--back">
    <div class="back-pattern" role="img" aria-label="Repeating tonal brand pattern across the card back"></div>
    <p class="back-brand">Harbourline Homes</p>
  </section>

  <section class="card card--front">
    <h1 class="holder-name">Daniel Reeves</h1>
    <p class="holder-role">Owner</p>
    <p class="address">42 Elmstead Avenue,<br>Riverton, Vic 3150</p>
    <ul class="contacts">
      <li class="contact">
        <svg class="contact-icon" viewBox="0 0 24 24" aria-hidden="true"><path d="M6.6 10.8a15.1 15.1 0 0 0 6.6 6.6l2.2-2.2a1 1 0 0 1 1-.25 11.4 11.4 0 0 0 3.6.57 1 1 0 0 1 1 1V20a1 1 0 0 1-1 1A17 17 0 0 1 3 4a1 1 0 0 1 1-1h3.5a1 1 0 0 1 1 1c0 1.25.2 2.45.57 3.6a1 1 0 0 1-.25 1z"/></svg>
        <span>0400 555 018</span>
      </li>
      <li class="contact">
        <svg class="contact-icon" viewBox="0 0 24 24" aria-hidden="true"><path d="M2 5h20v14H2z M2 5l10 8 10-8" fill="none" stroke="#2f80ff" stroke-width="0"/><path d="M2 5h20L12 12.5z"/><path d="M2 7.2l10 7.5 10-7.5V19H2z"/></svg>
        <span>info@harbourlinehomes.com</span>
      </li>
      <li class="contact">
        <svg class="contact-icon" viewBox="0 0 24 24" aria-hidden="true"><circle cx="12" cy="12" r="9" fill="none" stroke="#2f80ff" stroke-width="2"/><path d="M3 12h18M12 3c3 3.2 3 14.8 0 18M12 3c-3 3.2-3 14.8 0 18" fill="none" stroke="#2f80ff" stroke-width="1.6"/></svg>
        <span>www.harbourlinehomes.com</span>
      </li>
    </ul>
    <p class="front-brand">Harbourline Homes</p>
  </section>
</main>
</body>
</html>
```